Velmora Strom GmbH webpage The online Business card of a master electrician

A clean, modern webpage on whitch i can show my clients what im capable of and where the future costumer can inform himself. I need a login page for costumers who are registred and an secound webpage where my stuff can login to report theyr labour.
I will post pictures before and after, put on some commercial and crossellimg informations.
The costumer should find my insta as well my twitter or snapchat accounts.

Update:
Our Services are, Installations, Renovations, Home Automation, CCTV, Telefon / VOIP, Networking / Network-Cabeling, Electrical Supervisioning

Target Market(s)

Private and business costumers

Industry/Entity Type

Electric Company

Number of Pages Required

5+ page

Font styles to use
Sans Serif
Other font styles liked:
• Zurich,

Colors

Designer to choose colors to be used in the design.

Requirements
Must have
• A Page Hero
• A Costumer and staff login page (2separate pages)
• Contact form
• Responsive form
• Social Media enbedding account velmora_strom
Nice to have
• A Blog

```html
<!DOCTYPE html>
<html lang="en">
<head>
<meta charset="utf-8">
<title>Velmora Strom – Master Electrician</title>
<link rel="stylesheet" href="https://fonts.googleapis.com/css2?family=Lato:wght@400;700;900&family=Montserrat:wght@600;700;800&display=swap">
<style>
:root{
  --blue:#0b63c1;
  --blue-dark:#084f9c;
  --ink:#1b1b1b;
  --text:#4a4a4a;
  --muted:#8a8a8a;
  --paper:#ffffff;
  --stone:#efeee9;
  --line:#d9d9d9;
  --footer:#1b1b1b;
  --footer-bar:#0e0e0e;
}
*{box-sizing:border-box;margin:0;padding:0}
html,body{width:1200px;height:3734px;overflow:hidden}
body{font-family:"Lato",Arial,sans-serif;color:var(--text);background:var(--paper);position:relative}
section,header,footer{position:absolute;left:0;width:1200px}
.abs{position:absolute}
.btn{display:inline-block;font-family:"Montserrat",Arial,sans-serif;font-weight:700;font-size:14px;letter-spacing:.5px;text-transform:uppercase;color:#fff;text-align:center}
.btn-dark{background:var(--ink)}
.btn-blue{background:var(--blue)}

/* header */
.site-header{top:0;height:105px;background:#fff;border-bottom:1px solid #e6e6e6}
.brand{left:100px;top:18px;display:flex;align-items:center;gap:14px}
.brand-dot{width:44px;height:44px;border-radius:50%;background:var(--blue)}
.brand-name{font-family:"Montserrat",Arial,sans-serif;font-weight:800;font-size:34px;color:var(--blue-dark);letter-spacing:.5px}
.login-links{right:100px;top:14px;display:flex;gap:16px}
.login-links .btn{padding:11px 16px;font-size:12px}
.main-nav{right:100px;top:66px;display:flex}
.main-nav a{font-family:"Lato",Arial,sans-serif;font-weight:700;font-size:14px;color:#444;text-decoration:none;text-transform:uppercase;padding:0 21px;border-left:1px solid #ccc;line-height:16px}
.main-nav a:first-child{border-left:none}
.main-nav a.current{color:var(--blue);position:relative}
.main-nav a.current:after{content:"";position:absolute;left:50%;top:26px;margin-left:-5px;border:5px solid transparent;border-top-color:var(--blue)}

/* hero */
.hero{top:105px;height:547px;background:linear-gradient(180deg,#3f5d86 0%,#7b90aa 38%,#b59a82 56%,#2f3b4c 72%,#1c2634 100%)}
.hero-title{left:0;width:100%;bottom:22px;text-align:center;font-family:"Montserrat",Arial,sans-serif;font-weight:700;font-size:35px;letter-spacing:1.5px;color:#fff}
.hero-arrow{top:240px;width:60px;height:52px;background:#fff;display:flex;align-items:center;justify-content:center}
.hero-arrow.prev{left:0}.hero-arrow.next{right:0}

/* section headings */
.sec-title{font-family:"Montserrat",Arial,sans-serif;font-weight:800;font-size:30px;color:var(--ink);text-transform:uppercase;letter-spacing:.5px}
.sec-title em{font-style:normal;color:var(--blue)}
.centered{left:0;width:100%;text-align:center}
.divider{height:20px;display:flex;align-items:center;gap:10px}
.divider span{flex:1;height:1px;background:var(--line)}

/* services */
.services{top:652px;height:485px;background:#fff}
.service-card{top:133px;width:315px}
.service-photo{width:315px;height:200px;border:3px solid var(--blue);position:relative}
.service-badge{position:absolute;right:20px;bottom:-3px;width:74px;height:42px;background:var(--blue);border-radius:37px 37px 0 0;display:flex;align-items:center;justify-content:center}
.service-card h3{font-family:"Montserrat",Arial,sans-serif;font-weight:700;font-size:17px;color:var(--ink);text-align:center;margin-top:22px}
.service-card p{font-size:13px;line-height:21px;color:#555;text-align:center;margin-top:9px}
.service-card p b{color:var(--blue)}
.slider-nav{left:693px;top:58px;display:flex;gap:6px}
.slider-nav span{width:26px;height:26px;display:flex;align-items:center;justify-content:center}
.quote-box{left:797px;top:50px;width:303px;height:390px;background:#fff;box-shadow:0 6px 16px rgba(0,0,0,.2)}
.quote-head{height:60px;background:var(--blue);color:#fff;font-family:"Montserrat",Arial,sans-serif;font-weight:700;font-size:21px;text-align:center;line-height:60px}
.quote-form{padding:20px 20px 0}
.field{height:38px;border:1px solid #e2e2e2;background:#f7f7f7;margin-bottom:9px;font-size:12px;color:#888;padding:11px 12px}
.field.tall{height:68px}
.quote-form .btn{width:100%;height:38px;line-height:38px;margin-top:12px;font-size:15px}

/* about */
.about{top:1137px;height:366px;background:var(--stone)}
.about .lead{left:115px;width:970px;top:133px;text-align:center;font-weight:700;font-size:16px;line-height:24px;color:var(--ink)}
.about .lead span{font-weight:400;font-size:14px;color:#444}
.about .body{left:115px;width:970px;top:198px;text-align:center;font-size:14px;line-height:24px;color:#444}
.about .btn{left:538px;top:277px;width:124px;height:38px;line-height:38px;font-size:13px}

/* gallery */
.gallery{top:1503px;height:487px;background:#fff}
.shot{top:142px;width:228px;height:185px;border:3px solid var(--blue);border-radius:10px}
.shot-label{top:348px;width:228px;text-align:center;font-weight:700;font-size:16px;color:var(--ink)}
.gallery .btn{left:538px;top:402px;width:124px;height:36px;line-height:36px;font-size:13px}

/* why */
.why{top:1990px;height:560px;background:var(--stone);overflow:hidden}
.why-label{font-family:"Montserrat",Arial,sans-serif;font-weight:700;font-size:18px;color:var(--ink);text-transform:uppercase}
.why-center{left:460px;top:464px;width:280px;text-align:center;font-family:"Montserrat",Arial,sans-serif;font-weight:800;font-size:28px;color:#8d8d8d}

/* blog */
.blog{top:2550px;height:655px;background:#fff}
.post{top:138px;width:315px;height:392px;border:1px solid #dedede;background:#fff}
.post-photo{height:208px;position:relative}
.post-date{position:absolute;right:0;top:0;width:52px;height:48px;background:var(--blue);color:#fff;text-align:center;font-weight:900;font-size:20px;line-height:22px;padding-top:3px}
.post-date small{display:block;font-size:12px;font-weight:700;line-height:14px}
.post h4{margin:16px 18px 0;font-weight:700;font-size:16px;color:var(--ink)}
.post .by{margin:8px 18px 0;font-size:12px;color:#444}
.post .by b{color:var(--blue);font-weight:400}
.post p{margin:10px 18px 0;font-size:13px;line-height:20px;color:#555}
.post .btn{margin:12px 18px 0;width:110px;height:36px;line-height:36px;font-size:12px}
.blog-arrow{top:320px}
.blog .more{left:525px;top:565px;width:150px;height:36px;line-height:36px;font-size:13px}

/* social strip */
.social-strip{top:3205px;height:188px;background:#222}
.follow-cta{left:0;top:0;width:250px;height:188px;background:var(--blue);color:#fff;text-align:center;font-weight:700;font-size:18px;line-height:24px;padding-top:40px}
.follow-cta .ring{width:42px;height:42px;border:4px solid #fff;border-radius:50%;margin:0 auto 18px}
.tile{top:0;height:188px;width:188px;border-left:2px solid #111}

/* footer */
.site-footer{top:3393px;height:341px;background:var(--footer);color:#ddd}
.f-col{top:40px}
.f-col h5{font-family:"Montserrat",Arial,sans-serif;font-weight:700;font-size:17px;color:#fff;text-transform:uppercase;padding-bottom:12px;border-bottom:1px solid #3a3a3a}
.f-links{list-style:none;margin-top:14px}
.f-links li{font-size:14px;color:#e2e2e2;line-height:35px;padding-left:14px;position:relative}
.f-links li:before{content:"";position:absolute;left:0;top:16px;width:4px;height:4px;background:#fff;border-radius:50%}
.contact p{font-size:13px;line-height:18px;color:#ddd}
.contact .name{font-weight:700;color:#fff;margin-top:14px}
.contact .row{display:flex;align-items:center;gap:12px;margin-top:16px;font-size:13px}
.f-field{height:34px;border:1px solid #444;background:#151515;margin-top:9px;font-size:12px;color:#ccc;padding:10px 10px}
.f-field.tall{height:46px}
.f-col .btn{margin-top:14px;width:104px;height:34px;line-height:34px;font-size:13px}
.f-brand{left:870px;top:130px;width:240px;text-align:center;font-family:"Montserrat",Arial,sans-serif;font-weight:800;font-size:26px;color:#6f6f6f;white-space:nowrap}
.f-bar{left:0;bottom:0;width:1200px;height:44px;background:var(--footer-bar);font-size:13px;color:#ccc;padding:14px 100px}
.socials{right:100px;top:11px;display:flex;gap:8px}
.socials span{width:22px;height:22px;border-radius:50%;background:var(--blue)}
</style>
</head>
<body>

<header class="site-header">
  <div class="abs brand"><span class="brand-dot"></span><span class="brand-name">Velmora Strom</span></div>
  <div class="abs login-links">
    <span class="btn btn-blue">Costumer Login</span>
    <span class="btn btn-blue">Staff Login</span>
  </div>
  <nav class="abs main-nav">
    <a class="current">Home</a><a>About Us</a><a>Our Services</a><a>Photo Gallery</a><a>Contact Us</a>
  </nav>
</header>

<section class="hero" role="img" aria-label="Evening view of an old city along a river with church towers and lit waterfront">
  <span class="abs hero-arrow prev"><svg width="14" height="20" viewBox="0 0 14 20"><path d="M11 2 3 10l8 8" fill="none" stroke="#222" stroke-width="3"/></svg></span>
  <span class="abs hero-arrow next"><svg width="14" height="20" viewBox="0 0 14 20"><path d="M3 2l8 8-8 8" fill="none" stroke="#222" stroke-width="3"/></svg></span>
  <h1 class="abs hero-title">WE SPECIALIZED IN COMMERCIAL ELECTRICIAN</h1>
</section>

<section class="services">
  <h2 class="abs sec-title" style="left:100px;top:46px"><em>Our</em> Services</h2>
  <div class="abs divider" style="left:100px;top:89px;width:660px"><svg width="10" height="18" viewBox="0 0 10 18"><path d="M6 0 0 10h4l-2 8 8-11H6l2-7z" fill="#b5b5b5"/></svg><span></span></div>
  <div class="abs slider-nav">
    <span style="background:#ddd"><svg width="8" height="12" viewBox="0 0 8 12"><path d="M6 1 1 6l5 5" fill="none" stroke="#333" stroke-width="2"/></svg></span>
    <span style="background:var(--blue)"><svg width="8" height="12" viewBox="0 0 8 12"><path d="M2 1l5 5-5 5" fill="none" stroke="#fff" stroke-width="2"/></svg></span>
  </div>
  <article class="abs service-card" style="left:100px">
    <div class="service-photo" role="img" aria-label="Hand using a home automation tablet with floating smart-home symbols" style="background:linear-gradient(135deg,#e7eef6,#9fb3c9 60%,#5d7696)">
      <span class="service-badge"><svg width="28" height="26" viewBox="0 0 28 26"><path d="M14 2 2 13h4v11h7v-7h2v7h7V13h4z" fill="#fff"/></svg></span>
    </div>
    <h3>HOME AUTOMATION</h3>
    <p>Lorem ipsum dolor sit amet, consectetuer adipiscing elit, sed diam nonummy nibh eui tincidunt... <b>[ + ]</b></p>
  </article>
  <article class="abs service-card" style="left:443px">
    <div class="service-photo" role="img" aria-label="Electrician working with pliers on a switchboard full of cables" style="background:linear-gradient(135deg,#b8c4cf,#6f8397 55%,#39475a)">
      <span class="service-badge"><svg width="22" height="28" viewBox="0 0 22 28"><path d="M6 1v7M16 1v7M3 8h16v6a8 8 0 0 1-16 0zM11 22v5" fill="none" stroke="#fff" stroke-width="3"/></svg></span>
    </div>
    <h3>COMMERCIAL</h3>
    <p>Lorem ipsum dolor sit amet, consectetuer adipiscing elit, sed diam nonummy nibh eui tincidunt... <b>[ + ]</b></p>
  </article>
  <aside class="abs quote-box">
    <div class="quote-head">REQUEST A QUOTE</div>
    <form class="quote-form">
      <div class="field">Full Name</div>
      <div class="field">Email</div>
      <div class="field">Phone</div>
      <div class="field tall">Message</div>
      <span class="btn btn-dark">Submit</span>
    </form>
  </aside>
</section>

<section class="about">
  <h2 class="abs sec-title centered" style="top:46px"><em>About</em> Us</h2>
  <div class="abs divider" style="left:440px;top:89px;width:320px"><span></span><svg width="10" height="18" viewBox="0 0 10 18"><path d="M6 0 0 10h4l-2 8 8-11H6l2-7z" fill="#b5b5b5"/></svg><span></span></div>
  <p class="abs lead">Lorem ipsum dolor sit amet, consectetuer adipiscing elit, sed diam nonummy nibh eui tincidunt ut laoreet dolore magna aliquam eratisi enim ad minim veniam quis <span>Sed ut perspiciatis unde omnis iste natus error sit voluptatem accusantium doloremque .</span></p>
  <p class="abs body">Sed ut perspiciatis unde omnis iste natus error sit voluptatem accusantium doloremque laudantiu aperiam, eaque ipsa quae ab illo inventore veritatis et quasi architecto beatae vitae dicta sunt exp Nemo enim ipsam voluptatem quia voluptas sit aspernatur aut odit aut fugit.</p>
  <span class="abs btn btn-dark">Read More</span>
</section>

<section class="gallery">
  <h2 class="abs sec-title centered" style="top:46px"><em>Photo</em> Gallery</h2>
  <div class="abs divider" style="left:440px;top:89px;width:320px"><span></span><svg width="10" height="18" viewBox="0 0 10 18"><path d="M6 0 0 10h4l-2 8 8-11H6l2-7z" fill="#b5b5b5"/></svg><span></span></div>
  <div class="abs shot" style="left:100px;background:linear-gradient(160deg,#4a4034,#8b7a5e 55%,#2a2520)" role="img" aria-label="Lounge with armchairs before the lighting work"></div>
  <div class="abs shot" style="left:345px;background:linear-gradient(160deg,#5a5040,#b9a07a 55%,#3a3229)" role="img" aria-label="Lounge with armchairs after the lighting work"></div>
  <div class="abs shot" style="left:625px;background:linear-gradient(160deg,#6a5630,#a88b4f 50%,#5d4a2c)" role="img" aria-label="Kitchen with wooden cabinets before the renovation"></div>
  <div class="abs shot" style="left:872px;background:linear-gradient(160deg,#5f8a2a,#9cc455 50%,#6e5530)" role="img" aria-label="Kitchen with green walls after the renovation"></div>
  <div class="abs shot-label" style="left:100px">Before</div>
  <div class="abs shot-label" style="left:345px">After</div>
  <div class="abs shot-label" style="left:625px">Before</div>
  <div class="abs shot-label" style="left:872px">After</div>
  <svg class="abs" style="left:312px;top:345px" width="56" height="20" viewBox="0 0 56 20"><path d="M3 6q24 16 46 2" fill="none" stroke="var(--blue)" stroke-width="3"/><path d="M42 3l9 4-7 7" fill="none" stroke="var(--blue)" stroke-width="3"/></svg>
  <svg class="abs" style="left:838px;top:345px" width="56" height="20" viewBox="0 0 56 20"><path d="M3 6q24 16 46 2" fill="none" stroke="var(--blue)" stroke-width="3"/><path d="M42 3l9 4-7 7" fill="none" stroke="var(--blue)" stroke-width="3"/></svg>
  <span class="abs btn btn-dark">View All</span>
</section>

<section class="why">
  <h2 class="abs sec-title centered" style="top:46px"><em>Why</em> Choose Us</h2>
  <div class="abs divider" style="left:440px;top:89px;width:320px"><span></span><svg width="10" height="18" viewBox="0 0 10 18"><path d="M6 0 0 10h4l-2 8 8-11H6l2-7z" fill="#b5b5b5"/></svg><span></span></div>
  <svg class="abs" style="left:0;top:0" width="1200" height="560" viewBox="0 0 1200 560">
    <g stroke="var(--blue)" stroke-width="4">
      <line x1="600" y1="275" x2="600" y2="340"/>
      <line x1="455" y1="325" x2="488" y2="370"/>
      <line x1="745" y1="325" x2="712" y2="370"/>
      <line x1="378" y1="458" x2="425" y2="470"/>
      <line x1="822" y1="458" x2="775" y2="470"/>
    </g>
    <circle cx="600" cy="545" r="196" fill="#fff" stroke="var(--blue)" stroke-width="30"/>
    <g fill="#fff" stroke="var(--blue)" stroke-width="4">
      <circle cx="600" cy="233" r="42"/>
      <circle cx="423" cy="296" r="42"/>
      <circle cx="777" cy="296" r="42"/>
      <circle cx="337" cy="458" r="42"/>
      <circle cx="863" cy="458" r="42"/>
    </g>
    <g fill="none" stroke="#222" stroke-width="3.5" stroke-linejoin="round">
      <path d="M584 224l16 10 16-10v18l-16-8-16 8zM600 234v16"/>
      <rect x="406" y="287" width="34" height="24" rx="3"/><path d="M416 287v-6h14v6"/>
      <circle cx="777" cy="292" r="13"/><path d="M770 305l-6 14 7-3 4 6M784 305l6 14-7-3-4 6"/><path d="M771 292l5 5 8-9"/>
      <circle cx="863" cy="458" r="18"/><path d="M854 458l7 7 12-13"/>
    </g>
    <text x="337" y="471" text-anchor="middle" font-family="Montserrat,Arial,sans-serif" font-weight="800" font-size="38" fill="#222">$</text>
  </svg>
  <span class="abs why-label" style="left:555px;top:150px">Modern</span>
  <span class="abs why-label" style="left:245px;top:286px">Experience</span>
  <span class="abs why-label" style="left:833px;top:286px">Quality</span>
  <span class="abs why-label" style="left:187px;top:448px">Low Cost</span>
  <span class="abs why-label" style="left:918px;top:448px">Gaurantee</span>
  <div class="abs why-center">Velmora Strom</div>
</section>

<section class="blog">
  <h2 class="abs sec-title centered" style="top:46px"><em>Latest</em> Blog</h2>
  <div class="abs divider" style="left:440px;top:89px;width:320px"><span></span><svg width="10" height="18" viewBox="0 0 10 18"><path d="M6 0 0 10h4l-2 8 8-11H6l2-7z" fill="#b5b5b5"/></svg><span></span></div>
  <svg class="abs blog-arrow" style="left:48px" width="20" height="40" viewBox="0 0 20 40"><path d="M17 2 3 20l14 18" fill="none" stroke="#ccc" stroke-width="2"/></svg>
  <svg class="abs blog-arrow" style="left:1132px" width="20" height="40" viewBox="0 0 20 40"><path d="M3 2l14 18L3 38" fill="none" stroke="#ccc" stroke-width="2"/></svg>
  <article class="abs post" style="left:100px">
    <div class="post-photo" role="img" aria-label="Pencils and tools lying on building plans" style="background:linear-gradient(135deg,#f1efe9,#c9c4b8 60%,#8f877a)"><span class="post-date">13<small>JUN</small></span></div>
    <h4>Duis autem velopk eum iriure dolor</h4>
    <p class="by">By: <b>Lorem Ipsum Dolor</b></p>
    <p>Ut wisi enim ad minim veniam, quis nostrul exercimori more tationconsequat.</p>
    <span class="btn btn-blue">Read More</span>
  </article>
  <article class="abs post" style="left:443px">
    <div class="post-photo" role="img" aria-label="Hand plugging network cables into a server rack" style="background:linear-gradient(135deg,#3f6fa8,#7aa3cf 50%,#2b3d58)"><span class="post-date">13<small>JUN</small></span></div>
    <h4>Duis autem velopk eum iriure dolor</h4>
    <p class="by">By: <b>Lorem Ipsum Dolor</b></p>
    <p>Ut wisi enim ad minim veniam, quis nostrul exercimori more tationconsequat.</p>
    <span class="btn btn-blue">Read More</span>
  </article>
  <article class="abs post" style="left:785px">
    <div class="post-photo" role="img" aria-label="Smartphone smart-home app held in front of a modern house" style="background:linear-gradient(135deg,#cfe0ee,#9cb7cf 55%,#6d8a6a)"><span class="post-date">13<small>JUN</small></span></div>
    <h4>Duis autem velopk eum iriure dolor</h4>
    <p class="by">By: <b>Lorem Ipsum Dolor</b></p>
    <p>Ut wisi enim ad minim veniam, quis nostrul exercimori more tationconsequat.</p>
    <span class="btn btn-blue">Read More</span>
  </article>
  <span class="abs btn btn-dark more">View All Blog</span>
</section>

<section class="social-strip">
  <div class="abs follow-cta"><div class="ring"></div>Follow Us on<br>Social Media</div>
  <div class="abs tile" style="left:250px;background:linear-gradient(160deg,#6b4a34,#c9a98a 55%,#3a2a20)" role="img" aria-label="Restaurant interior with set tables"></div>
  <div class="abs tile" style="left:440px;background:linear-gradient(160deg,#4a3a2a,#d7a24a 50%,#2a2018)" role="img" aria-label="Warmly lit dining room"></div>
  <div class="abs tile" style="left:630px;background:linear-gradient(160deg,#3a2e26,#9c7f66 55%,#211a15)" role="img" aria-label="Restaurant with ceiling lights"></div>
  <div class="abs tile" style="left:820px;background:linear-gradient(160deg,#d9d6d0,#8e8a84 55%,#3a3632)" role="img" aria-label="Cup of coffee on a table"></div>
  <div class="abs tile" style="left:1010px;width:190px;background:linear-gradient(160deg,#5a3e2c,#b8927a 55%,#2e2018)" role="img" aria-label="Restaurant tables with red chairs"></div>
  <span class="abs" style="left:258px;top:82px;width:24px;height:24px;background:rgba(0,0,0,.6)"></span>
  <span class="abs" style="left:1168px;top:82px;width:24px;height:24px;background:rgba(0,0,0,.6)"></span>
</section>

<footer class="site-footer">
  <div class="abs f-col" style="left:100px;width:170px">
    <h5>Quick Links</h5>
    <ul class="f-links"><li>Home</li><li>About Us</li><li>Our Services</li><li>Photo Gallery</li><li>Contact Us</li></ul>
  </div>
  <div class="abs f-col contact" style="left:307px;width:210px">
    <h5>Contact Details</h5>
    <p class="name">Velmora Strom</p>
    <p>48 Kelber Lane,<br>Norhaven - 10482</p>
    <div class="row"><svg width="14" height="14" viewBox="0 0 14 14"><path d="M3 1l3 3-2 2q2 3 4 4l2-2 3 3-2 2Q5 12 1 3z" fill="#ddd"/></svg>012-555-0147</div>
    <div class="row"><svg width="14" height="14" viewBox="0 0 14 14"><path d="M3 1l3 3-2 2q2 3 4 4l2-2 3 3-2 2Q5 12 1 3z" fill="#ddd"/></svg>012-555-0147</div>
    <div class="row"><svg width="14" height="12" viewBox="0 0 14 12"><rect x="1" y="1" width="12" height="10" fill="#ddd"/><path d="M1 1l6 5 6-5" fill="none" stroke="#1b1b1b" stroke-width="1.5"/></svg>info@velmorastrom.com</div>
  </div>
  <div class="abs f-col" style="left:580px;width:260px">
    <h5>Quick Inquiry</h5>
    <div class="f-field" style="margin-top:16px">Name</div>
    <div class="f-field">Email</div>
    <div class="f-field tall">Message</div>
    <span class="btn btn-blue">Submit</span>
  </div>
  <div class="abs f-brand">Velmora Strom</div>
  <div class="abs f-bar">Copyright © 2017 Velmora Strom. All Right Reserved.
    <div class="abs socials"><span></span><span></span><span></span></div>
  </div>
</footer>

</body>
</html>
```